Web design for new streaming audio service

We need a homepage design for a new streaming audio service. Our company is called Olvantra, and we’re basically Vidorama for Audiobooks, Stand-Up Comedy, Lectures, Language Learning, etc. Essentially like Tunelark for everything audio EXCEPT music.
You don’t have to code the homepage (Design Only), but it should include 3 different designs to work with 1) Web; 2) Phones; 3) Tablets.
Below is a link to a mockup of the web version which gives a good idea of what elements we want. This is just a mockup and we want you to improve it.
Once you download the mockup, please refer to the more detailed instructions below:
The following outlines the design project for the Olvantra homepage. We have provided a rough mockup of the homepage layout that gives you a general idea of what we’re going for. There are a few elements that we are attached to, and many others where you have complete creative freedom to do whatever you think looks good.
The ZIP file includes the following:
* Mockup to see what we have in mind (olvantra-homepage-mockup.jpg)
* Text used (olvantra-homepage-text.txt)
* Raw image of actor (olvantra-actor1.jpg)
* Raw images for samples (olvantra-sample-[name].jpg)
Although we have only provided a mockup layout for the web version, we also need you to provide a mobile phone and a tablet version of the design also. It’s very possible the tablet version may be substantially similar to the web version, but the mobile phone version will likely be much different.
All of the raw files are included in the attached ZIP file. Please use our photographs and text as provided although cropping, sizing, etc. is flexible per the instructions below.
Display Requirements:
* Web Version - Minimum resolution 1024x768 (72 dpi) but should look good on 1920x1080 (72 dpi) - Page should be designed to scale to look acceptable in all resolutions in between.
* Phone Version - Minimum Zentro 4 - 640x960 (326 dpi) but should look good on Korvel Nimbus Q5 - 1920x1080 (441 dpi) - Page should be designed to scale to look acceptable in all resolutions and devices in between.
* Tablet Version - Minimum Pagewick Ember LX 7” - 1280x800 (216 dpi) but should also look good on a Slato Breeze - 2048x1536 (264 dpi) - Page should be designed to scale to look acceptable in all resolutions and devices in between.
Above the Fold - We want to make sure the Olvantra logo, Member Login Link, Large Photo, Headline, Price, Button, and the first row of sample images are all “Above the fold”. As a general guideline, this means 600 pixels high on a 1024x768 72 dpi web screen. This requirement is less important on Phone versions.
Top Logo Bar - We want to retain the blue bar with the Olvantra logo on the page, although we are open to a different size, shape and positioning if it greatly enhances the design. Please use the standard logo color, although you are welcome to use either the horizontal or vertical orientation of the logo based on your design.
Text color, font and size - Feel free to design the text in anyway you choose as long as the text is readable on the target platforms.
Buttons - Feel free to use any size, shape and colors for the buttons as long as they are obvious and clickable relative to the page. The only exception is the Chatterly button should follow the Chatterly color scheme and logo treatment (the mockup doesn’t seem 100% correct.)
Top Photograph - We want to retain the large photograph across the top of the screen although final shape and dimensions are flexible.
Size and shape of content samples (i.e. Audiobooks, Stand-Up Comedy, etc.) - Feel free to design the content samples in anyway you choose.
Three Sales Points (i.e. Listen on your Zentro…, All you can enjoy…, etc.) - The Three Sales Points are envisioned to each have a corresponding illustration which you should provide and have rights for. The placeholder is represented by a square next to the text. The color size and shape of these elements are flexible and can be designed in any way you choose.
Opt-in form - Feel free to design the opt-in form in anyway you choose as long as the text is readable and the interactivity is obvious on the target platforms.
Text links and copyright notice - Feel free to design the bottom of the page text links and copyright notice in anyway you choose.
Additional colors, graphic design elements, etc. - Feel free to use any additional colors, graphic design elements, etc. to support your design.

```html
<!DOCTYPE html>
<html lang="en">
<head>
<meta charset="utf-8">
<title>Olvantra – Unlimited listening</title>
<link href="https://fonts.googleapis.com/css2?family=Open+Sans:wght@300;400;600&display=swap" rel="stylesheet">
<style>
:root{
  --brand-blue:#5aa9d4;
  --heading-blue:#4a9fcf;
  --price-red:#c23a3c;
  --navy:#3a4565;
  --text:#5f5f5f;
  --muted:#8a8a8a;
  --band:#f4f4f4;
  --line:#dedede;
  --card:#efefef;
  --play:#5aa3b8;
  --btn-gray:#676767;
  --social:#3b5a9a;
  --footer:#2c2c2c;
  --footer-text:#bdbdbd;
}
*{box-sizing:border-box;margin:0;padding:0}
html,body{width:874px;height:1200px;overflow:hidden;background:#fff}
body{position:relative;font-family:"Open Sans",sans-serif;color:var(--text)}
h1,h2,p{font-weight:400}
.abs{position:absolute}

.hero{left:0;top:0;width:874px;height:446px;
  background:
    radial-gradient(ellipse 170px 210px at 250px 250px,rgba(224,176,146,.95),rgba(214,160,126,.6) 55%,rgba(214,160,126,0) 100%),
    radial-gradient(ellipse 150px 120px at 230px 130px,rgba(170,120,80,.75),rgba(170,120,80,0) 100%),
    radial-gradient(ellipse 120px 110px at 370px 400px,rgba(235,232,228,.9),rgba(235,232,228,0) 100%),
    radial-gradient(ellipse 300px 150px at 120px 440px,rgba(72,86,112,.95),rgba(72,86,112,0) 100%),
    radial-gradient(ellipse 220px 170px at 640px 470px,rgba(80,96,124,.85),rgba(80,96,124,0) 100%),
    linear-gradient(90deg,#8a7c74 0%,#c7a58c 18%,#e7d6c8 40%,#f6f3f0 56%,#fbfbfb 100%)}
.topbar{left:72px;top:0;width:730px;height:56px;background:var(--brand-blue);box-shadow:0 2px 2px rgba(0,0,0,.2)}
.brand{left:11px;top:12px;display:flex;align-items:center;gap:7px;color:#fff;font-size:25px;font-weight:400;letter-spacing:-.5px}
.brand-mark{width:20px;height:20px;border-radius:50%;background:#fff}
.login{right:12px;top:15px;width:87px;height:23px;background:#fff;border-radius:2px;font-size:10px;color:#555;display:flex;align-items:center;justify-content:center}
.headline{right:92px;top:136px;text-align:right;font-weight:300;font-size:34px;line-height:37px;color:#6a6a6a}
.price{right:99px;top:220px;font-size:21px;color:var(--price-red)}
.cta{left:583px;top:251px;width:196px;height:33px;background:var(--navy);color:#fff;border-radius:2px;font-size:15px;font-weight:600;display:flex;align-items:center;justify-content:center;letter-spacing:.2px}
.cta-note{right:95px;top:290px;font-size:10px;color:#666}
.dots{left:400px;top:421px;width:74px;height:16px;border-radius:8px;background:rgba(70,70,70,.7);display:flex;align-items:center;justify-content:center;gap:8px}
.dots i{width:7px;height:7px;border-radius:50%;background:#fff}
.dots i:first-child{background:transparent;border:1.5px solid #fff}

.samples-title{left:0;width:874px;top:474px;text-align:center;font-size:18.5px;font-weight:400;color:var(--heading-blue)}
.card{width:166px;height:143px;background:var(--card);border:1px solid #dcdcdc}
.cover{position:absolute;left:4px;top:4px;width:157px;height:93px}
.card-title{position:absolute;left:10px;top:104px;font-size:12px;color:#555}
.card-len{position:absolute;left:10px;top:122px;font-size:9px;color:var(--muted)}
.play{position:absolute;left:137px;top:110px}

.points{left:0;top:856px;width:874px;height:114px;background:var(--band);border-top:1px solid var(--line);border-bottom:1px solid var(--line)}
.point-icon{width:76px;height:76px;border-radius:50%;background:#fff;border:1px solid #e4e4e4;display:flex;align-items:center;justify-content:center}
.point-text{font-size:13px;line-height:17px;color:#666}

.trial-title{left:103px;top:993px;font-size:19px;font-weight:400;color:var(--heading-blue)}
.trial-copy{left:104px;top:1020px;width:230px;font-size:10px;line-height:15.5px;color:#555}
.trial-note{left:103px;top:1069px;font-size:12px;color:var(--price-red)}
.email{left:346px;top:1022px;width:227px;height:30px;border:1px solid #d6d6d6;background:#fff;font-size:10px;color:#999;padding-left:11px;display:flex;align-items:center}
.access{left:590px;top:1022px;width:120px;height:30px;background:var(--btn-gray);color:#fff;font-size:12px;border-radius:2px;display:flex;align-items:center;justify-content:center}
.or{left:722px;top:1030px;font-size:12px;color:#888}
.social-btn{left:590px;top:1058px;width:180px;height:29px;background:var(--social);color:#fff;font-size:12px;border-radius:2px;display:flex;align-items:center;gap:10px;padding-left:8px}
.social-btn b{width:17px;height:17px;background:#fff;opacity:.9;border-radius:2px}

.footer{left:0;top:1116px;width:874px;height:84px;background:var(--footer)}
.footer-links{left:74px;top:22px;font-size:10.5px;color:var(--footer-text)}
.footer-links span{margin:0 8px;color:#777}
.copyright{left:74px;top:46px;font-size:10.5px;color:var(--footer-text)}
.footer-square{left:778px;top:30px;width:22px;height:22px;background:#4c6fb0;border-radius:2px}
</style>
</head>
<body>

<div class="abs hero" role="img" aria-label="Photo of a smiling young man wearing headphones and holding a phone"></div>

<header class="abs topbar">
  <div class="abs brand"><span class="brand-mark"></span>Olvantra</div>
  <div class="abs login">MEMBER LOGIN</div>
</header>

<h1 class="abs headline">Unlimited listening.<br>Wherever you are.</h1>
<div class="abs price">Only $9.99 per month</div>
<div class="abs cta">START YOUR FREE TRIAL</div>
<div class="abs cta-note">* Credit Card Not Required</div>
<div class="abs dots"><i></i><i></i><i></i><i></i></div>

<h2 class="abs samples-title">A Sample of What you can listen to on Olvantra</h2>

<div class="abs card" style="left:80px;top:518px"><div class="cover" role="img" aria-label="Album cover: singer in a blue hat" style="background:radial-gradient(ellipse 45px 55px at 45px 45px,#e6cfa6,rgba(230,207,166,0)),radial-gradient(ellipse 40px 30px at 125px 30px,#3d5a3a,rgba(61,90,58,0)),linear-gradient(120deg,#3f74b4,#9fb3c4 40%,#e0e0dc 70%,#2b3526)"></div><div class="card-title">Maecenas placerat</div><div class="card-len">3.8 mints</div><svg class="play" width="20" height="20"><circle cx="10" cy="10" r="9.5" fill="var(--play)"/><path d="M8 6l6 4-6 4z" fill="#333"/></svg></div>
<div class="abs card" style="left:262px;top:518px"><div class="cover" role="img" aria-label="Album cover: band crossing a street" style="background:linear-gradient(180deg,#5f7466 0%,#7f8a78 35%,#a4a396 55%,#6c6a62 80%,#4a4742 100%)"></div><div class="card-title">Maecenas placerat</div><div class="card-len">3.8 mints</div><svg class="play" width="20" height="20"><circle cx="10" cy="10" r="9.5" fill="var(--play)"/><path d="M8 6l6 4-6 4z" fill="#333"/></svg></div>
<div class="abs card" style="left:445px;top:518px"><div class="cover" role="img" aria-label="Album cover: singer in a white suit" style="background:radial-gradient(ellipse 55px 40px at 120px 75px,#f2efea,rgba(242,239,234,0)),linear-gradient(120deg,#1e1917,#4a3c34 45%,#6b5a4e 65%,#d9d4cd)"></div><div class="card-title">Maecenas placerat</div><div class="card-len">3.8 mints</div><svg class="play" width="20" height="20"><circle cx="10" cy="10" r="9.5" fill="var(--play)"/><path d="M8 6l6 4-6 4z" fill="#333"/></svg></div>
<div class="abs card" style="left:627px;top:518px"><div class="cover" role="img" aria-label="Album cover: black and white band photo" style="background:radial-gradient(ellipse 45px 45px at 78px 55px,#d8d8d8,rgba(216,216,216,0)),linear-gradient(120deg,#2e2e2e,#8a8a8a 45%,#c9c9c9 70%,#5a5a5a)"></div><div class="card-title">Maecenas placerat</div><div class="card-len">3.8 mints</div><svg class="play" width="20" height="20"><circle cx="10" cy="10" r="9.5" fill="var(--play)"/><path d="M8 6l6 4-6 4z" fill="#333"/></svg></div>

<div class="abs card" style="left:80px;top:677px"><div class="cover" role="img" aria-label="Album cover: young singer portrait" style="background:radial-gradient(ellipse 45px 45px at 45px 60px,#e8c3a6,rgba(232,195,166,0)),radial-gradient(ellipse 50px 35px at 120px 30px,#c8453a,rgba(200,69,58,0)),linear-gradient(120deg,#5a321e,#b98266 45%,#d8b49a 70%,#8a5a44)"></div><div class="card-title">Maecenas placerat</div><div class="card-len">3.8 mints</div><svg class="play" width="20" height="20"><circle cx="10" cy="10" r="9.5" fill="var(--play)"/><path d="M8 6l6 4-6 4z" fill="#333"/></svg></div>
<div class="abs card" style="left:262px;top:677px"><div class="cover" role="img" aria-label="Album cover: singer in a sunlit street" style="background:radial-gradient(ellipse 30px 40px at 35px 70px,#5a4a32,rgba(90,74,50,0)),linear-gradient(110deg,#a47c44,#efd6a4 45%,#f3e2bf 60%,#c08a5a)"></div><div class="card-title">Maecenas placerat</div><div class="card-len">3.8 mints</div><svg class="play" width="20" height="20"><circle cx="10" cy="10" r="9.5" fill="var(--play)"/><path d="M8 6l6 4-6 4z" fill="#333"/></svg></div>
<div class="abs card" style="left:445px;top:677px"><div class="cover" role="img" aria-label="Photo of a singer performing on stage" style="background:radial-gradient(ellipse 30px 40px at 20px 60px,#f1d9a0,rgba(241,217,160,0)),radial-gradient(ellipse 30px 40px at 140px 60px,#f1d9a0,rgba(241,217,160,0)),linear-gradient(180deg,#c5361f,#4a2018 40%,#241a18 75%,#151515)"></div><div class="card-title">Maecenas placerat</div><div class="card-len">3.8 mints</div><svg class="play" width="20" height="20"><circle cx="10" cy="10" r="9.5" fill="var(--play)"/><path d="M8 6l6 4-6 4z" fill="#333"/></svg></div>
<div class="abs card" style="left:627px;top:677px"><div class="cover" role="img" aria-label="Album cover: city skyline at sunset" style="background:radial-gradient(ellipse 50px 30px at 70px 30px,#ffe28a,rgba(255,226,138,0)),linear-gradient(180deg,#f7b233,#ea7a22 50%,#b8401a 75%,#4a1a10)"></div><div class="card-title">Maecenas placerat</div><div class="card-len">3.8 mints</div><svg class="play" width="20" height="20"><circle cx="10" cy="10" r="9.5" fill="var(--play)"/><path d="M8 6l6 4-6 4z" fill="#333"/></svg></div>

<section class="abs points">
  <div class="abs point-icon" style="left:82px;top:19px"><svg width="34" height="28" viewBox="0 0 34 28" fill="none" stroke="#777" stroke-width="2"><rect x="9" y="2" width="23" height="17"/><rect x="12" y="10" width="10" height="16" fill="#fff"/><rect x="2" y="13" width="7" height="12"/></svg></div>
  <div class="abs point-text" style="left:166px;top:38px">Listen on your Zentro,<br>Slato or Robolt device</div>
  <div class="abs point-icon" style="left:362px;top:19px"><svg width="34" height="40" viewBox="0 0 34 40"><path d="M12 4l5 4 5-4-2 8h-6z" fill="#666"/><path d="M13 12h8c8 6 12 14 10 20-1 4-5 6-14 6S4 36 3 32c-2-6 2-14 10-20z" fill="#666"/><text x="17" y="32" text-anchor="middle" font-family="Open Sans,sans-serif" font-size="14" fill="#fff">$</text></svg></div>
  <div class="abs point-text" style="left:446px;top:30px">All you can enjoy<br>for one low monthly<br>price.</div>
  <div class="abs point-icon" style="left:612px;top:19px"><svg width="36" height="36" viewBox="0 0 36 36" fill="none" stroke="#777" stroke-width="2.5"><circle cx="18" cy="18" r="15"/><path d="M18 9v9l6 6"/></svg></div>
  <div class="abs point-text" style="left:697px;top:38px">No obligation<br>Cancel any time.</div>
</section>

<h2 class="abs trial-title">Start your Free Trial</h2>
<p class="abs trial-copy">You will get instant &amp; unlimited access to all the material on Olvantra for 14 days. There is no obligation &amp; you can cancel at any time.</p>
<div class="abs trial-note">Credit Card Not Required for FREE TRIAL</div>
<div class="abs email">Your Email Address</div>
<div class="abs access">Get Instant Access</div>
<div class="abs or">Or</div>
<div class="abs social-btn"><b></b>Sign Up Using Chatterly</div>

<footer class="abs footer">
  <div class="abs footer-links">About<span>|</span>Help<span>|</span>Contact us<span>|</span>Member Login<span>|</span>Privacy Policy<span>|</span>Terms of Service</div>
  <div class="abs copyright">Copyright &nbsp;©&nbsp; 2014 &nbsp;Olvantra LLC. &nbsp;All rights reserved</div>
  <div class="abs footer-square" aria-label="Chatterly"></div>
</footer>

</body>
</html>
```